Brochure design for 3D ultrasound company

I am looking for a clean and modern and edgy brochure for my ultrasound company. We are a fairly new company specialize in 3D/4D ultrasounds.Our brochures will be placed in OB-GYN offices in high end areas around Los Angeles, so we need something that will stand out and capture a modern woman's attention. Our logo is currently in the process of being designed, so I don't have a picture to provide quite yet, however it will be our company name"Kite + Fern" written in a special font that looks like neon lights. I will attach a few images of what our logo will be like, and some initial content that can help provide the layout we would like for the brochure. please feel free to also take a look at our website. www.kitefernscans.example.

Target Market(s)

Upscale trendy women.

Colors
eea4c8
33a6d7
fee18a

Requirements
Should not have
• too many colors.

```html
<!DOCTYPE html>
<html lang="en">
<head>
<meta charset="utf-8">
<title>Kite + Fern – Trifold Brochure</title>
<link href="https://fonts.googleapis.com/css2?family=Cabin:ital,wght@0,400;0,600;0,700;1,400&family=Archivo+Black&display=swap" rel="stylesheet">
<style>
  :root{
    --hot-pink:#e41fc4;
    --blush:#eea4c8;
    --sky:#5aaedb;
    --sky-deep:#3f97c8;
    --lilac:#cdb9ec;
    --mint:#c9e6ef;
    --peach:#f6c3c0;
    --ink:#1e1e24;
    --white:#ffffff;
    --page:#ececef;
    --pastel:linear-gradient(150deg,#f4c6e4 0%,#d9c4f1 30%,#c8e2f3 55%,#f3c2df 78%,#e5d3f5 100%);
  }
  *{box-sizing:border-box;margin:0;padding:0}
  html,body{width:1095px;height:1200px;overflow:hidden}
  body{background:var(--page);font-family:"Cabin",sans-serif;color:var(--ink);position:relative}
  .panel{position:absolute;overflow:hidden}
  .outside{top:20px;height:580px}
  .inside{top:620px;height:560px}
  .pastel{background:var(--pastel)}
  .photo{position:absolute;border-radius:2px}
  .brand-name{font-family:"Cabin",sans-serif;font-weight:700;color:var(--hot-pink);text-align:center;letter-spacing:1px}

  /* Outside flap */
  .flap{left:30px;width:345px;padding:26px 24px}
  .flap-title{font-family:"Archivo Black",sans-serif;color:var(--hot-pink);font-size:30px;line-height:1.02;text-align:right;text-transform:uppercase}
  .flap-copy{font-size:13px;line-height:1.35;margin-top:18px}
  .flap-copy p+p{margin-top:12px}
  .flap .photo{left:24px;right:24px;bottom:24px;height:220px;background:linear-gradient(90deg,#f2b7c4 0%,#e8c3b0 35%,#cfe1d9 60%,#9fbfdc 100%)}

  /* Back panel */
  .back{left:375px;width:345px;padding:22px 26px}
  .back .photo{left:80px;top:22px;width:170px;height:230px;background:linear-gradient(180deg,#f4f2f2 0%,#e9d8cf 55%,#7fa0c4 100%)}
  .back .brand-name{position:absolute;left:0;right:0;top:268px;font-size:40px}
  .contact{position:absolute;left:26px;right:20px;top:345px;list-style:none}
  .contact li{display:flex;align-items:center;gap:12px;margin-bottom:12px;font-size:13px}
  .contact li svg{flex:0 0 24px}
  .contact .area{font-style:italic;font-size:13px;line-height:1.3}
  .contact .phone{font-size:24px;letter-spacing:1px}
  .dot-mark{width:22px;height:22px;border-radius:5px;background:var(--hot-pink);flex:0 0 22px;margin-left:1px}

  /* Front panel */
  .front{left:720px;width:345px}
  .front .tagline{position:absolute;right:22px;top:16px;text-align:center;font-size:13px;line-height:1.1}
  .front .brand-name{position:absolute;left:60px;right:10px;top:70px;font-size:44px}
  .front .photo{left:0;right:0;top:140px;height:330px;background:linear-gradient(180deg,#a39a9c 0%,#c9907a 30%,#eee6f0 55%,#f4eef4 80%,#bcd1e6 100%)}
  .front .headline{position:absolute;left:0;right:0;top:422px;text-align:center;font-family:"Archivo Black",sans-serif;font-size:13px;color:var(--white);letter-spacing:.5px;line-height:1.25}
  .front .call{position:absolute;left:0;right:0;top:476px;text-align:center;font-size:34px;letter-spacing:-1px}
  .front .call-phone{position:absolute;left:0;right:0;top:518px;text-align:center;font-family:"Archivo Black",sans-serif;font-size:30px;color:var(--hot-pink)}

  /* Inside spread */
  .spread{left:30px;width:690px;background:var(--sky)}
  .spread .photo.top{left:16px;top:16px;width:200px;height:110px;background:linear-gradient(90deg,#c89a86 0%,#e8c7b8 40%,#7d93b8 75%,#d7b5a3 100%)}
  .spread .brand-name{position:absolute;left:230px;right:20px;top:40px;font-size:46px}
  .available{position:absolute;left:180px;right:20px;top:120px;text-align:center;font-weight:700;font-size:11px;line-height:1.3;text-transform:uppercase}
  .popular{position:absolute;left:22px;top:140px;font-family:"Archivo Black",sans-serif;font-size:14px;line-height:1;color:var(--hot-pink);text-transform:uppercase}
  .packages{position:absolute;left:10px;right:10px;top:185px;display:grid;grid-template-columns:repeat(4,1fr);gap:8px}
  .package{text-align:center;color:var(--ink)}
  .package h3{font-family:"Archivo Black",sans-serif;font-size:13px;line-height:1;text-transform:uppercase;min-height:28px;color:var(--white)}
  .package .note{font-style:italic;font-size:10px;color:#e9f4fb;margin-top:-12px;margin-bottom:4px}
  .package ul{list-style:none;font-size:12px;line-height:1.15;color:#1d3a52}
  .package li{margin-bottom:7px}
  .package li::before{content:"• "}
  .price{position:absolute;top:425px;width:160px;text-align:center;font-size:20px;color:var(--white)}
  .spread .photo.band{left:0;right:0;bottom:0;height:82px;background:linear-gradient(90deg,#f6c3c0,#f1b8ad,#f6c3c0,#f0b4aa,#f6c3c0)}

  .guide{left:720px;width:345px;padding:22px 22px 0}
  .guide-title{font-family:"Archivo Black",sans-serif;font-style:normal;color:var(--hot-pink);font-size:22px;text-align:right}
  .guide dl{font-size:12px;line-height:1.3;text-align:right;margin-top:10px}
  .guide dt{display:inline;font-weight:700}
  .guide dd{display:inline;font-style:italic}
  .guide .entry{margin-bottom:10px}
  .guide .photo{left:22px;bottom:20px;width:150px;height:150px;background:linear-gradient(180deg,#f4efe9 0%,#e9c7ad 50%,#d8ab8d 100%)}
  .guide .closing{position:absolute;right:22px;bottom:24px;width:140px;text-align:right;font-size:12px;line-height:1.3;font-style:italic}
  .guide .closing strong{font-style:normal}
</style>
</head>
<body>

<!-- Outside: flap, back, front -->
<section class="panel outside flap pastel">
  <h2 class="flap-title">Ready for your baby's first photo shoot?</h2>
  <div class="flap-copy">
    <p>KITE + FERN is a mobile 3D ultrasound company servicing Los Angeles, and surrounding areas. We take great pride in being one of LA's first mobile ultrasound companies and for being an all female business!</p>
    <p>Our mission is to provide an unforgettable experience for expectant mothers in the comfort of their home!</p>
  </div>
  <div class="photo" role="img" aria-label="Photo of two expectant mothers in tees and jeans showing their bellies"></div>
</section>

<section class="panel outside back pastel">
  <div class="photo" role="img" aria-label="Photo of a pregnant woman in a white tee covering one eye"></div>
  <div class="brand-name">Kite + Fern</div>
  <ul class="contact">
    <li>
      <svg width="24" height="28" viewBox="0 0 24 28"><path d="M12 2a8 8 0 0 0-8 8c0 6 8 14 8 14s8-8 8-14a8 8 0 0 0-8-8z" fill="none" stroke="var(--hot-pink)" stroke-width="2"/><circle cx="12" cy="10" r="3" fill="var(--hot-pink)"/></svg>
      <span class="area">We currently service Los Angeles County, Orange County, and Ventura County</span>
    </li>
    <li>
      <svg width="24" height="28" viewBox="0 0 24 28"><rect x="6" y="2" width="12" height="24" rx="2" fill="none" stroke="var(--hot-pink)" stroke-width="2"/><line x1="10" y1="22" x2="14" y2="22" stroke="var(--hot-pink)" stroke-width="2"/></svg>
      <span class="phone">(555) 014-2288</span>
    </li>
    <li>
      <svg width="24" height="24" viewBox="0 0 24 24"><circle cx="12" cy="12" r="10" fill="none" stroke="var(--hot-pink)" stroke-width="2"/><ellipse cx="12" cy="12" rx="4" ry="10" fill="none" stroke="var(--hot-pink)" stroke-width="1.5"/><line x1="2" y1="12" x2="22" y2="12" stroke="var(--hot-pink)" stroke-width="1.5"/></svg>
      <span>www.kitefernscans.example</span>
    </li>
    <li>
      <svg width="24" height="20" viewBox="0 0 24 20"><rect x="1" y="2" width="22" height="16" fill="none" stroke="var(--hot-pink)" stroke-width="2"/><path d="M1 2l11 9 11-9" fill="none" stroke="var(--hot-pink)" stroke-width="2"/></svg>
      <span>info@kitefernscans.example</span>
    </li>
    <li><span class="dot-mark"></span><span>kite-fern</span></li>
    <li><span class="dot-mark"></span><span>@kitefernscans</span></li>
  </ul>
</section>

<section class="panel outside front pastel">
  <p class="tagline">A mobile 3D/4D<br>ultrasound<br>service</p>
  <div class="photo" role="img" aria-label="Photo of a pregnant woman holding an ultrasound print strip above her head"></div>
  <div class="brand-name">Kite + Fern</div>
  <p class="headline">ULTRASOUND IN THE<br>COMFORT OF YOUR HOME</p>
  <p class="call">CALL TODAY!</p>
  <p class="call-phone">555-014-2288</p>
</section>

<!-- Inside: packages spread and guide -->
<section class="panel inside spread">
  <div class="photo top" role="img" aria-label="Photo of a couple holding boy and girl notes over a pregnant belly"></div>
  <div class="brand-name">Kite + Fern</div>
  <p class="available">Available for private, in-home screenings, gender reveals,<br>baby showers, or any other special occasions!</p>
  <p class="popular">Our most<br>popular<br>package!</p>
  <div class="packages">
    <article class="package">
      <h3>The Big<br>Reveal:</h3>
      <ul>
        <li>25-minute 3D/4D/HD live session</li>
        <li>5 black &amp; white pictures</li>
        <li>5 color pictures</li>
        <li>Email or USB flash drive with all images</li>
        <li>Record &amp; hear heartbeat</li>
        <li>Confirm gender</li>
      </ul>
    </article>
    <article class="package">
      <h3>Hello<br>Mama:</h3>
      <ul>
        <li>15-minute 3D/4D/HD live session</li>
        <li>3 black &amp; white pictures</li>
        <li>2 color pictures</li>
        <li>Listen to baby's heartbeat</li>
        <li>Confirm gender</li>
      </ul>
    </article>
    <article class="package">
      <h3>V.I.B.</h3>
      <p class="note">(very important baby)</p>
      <ul>
        <li>30-minute 3D/4D/HD live session on our projector</li>
        <li>10 color pictures</li>
        <li>Email or USB with all images</li>
        <li>Listen to baby's heartbeat</li>
        <li>Confirm gender</li>
      </ul>
    </article>
    <article class="package">
      <h3>Peek-a-boo:</h3>
      <ul>
        <li>15-minute 2D session</li>
        <li>3 black &amp; white pictures</li>
        <li>Listen to baby's heartbeat</li>
        <li>Confirm gender</li>
      </ul>
    </article>
  </div>
  <p class="price" style="left:10px">$225.00</p>
  <p class="price" style="left:178px">$165.00</p>
  <p class="price" style="left:346px">$325.00</p>
  <p class="price" style="left:514px">$125.00</p>
  <div class="photo band" role="img" aria-label="Photo of a row of baby dolls on a pink background"></div>
</section>

<section class="panel inside guide pastel">
  <h2 class="guide-title">WHAT'S WHAT ...</h2>
  <dl>
    <div class="entry"><dt>2D</dt> <dd>is the traditional black-and-white photo - You know, the one that you want to get emotional about, but you don't know what you're looking at.</dd></div>
    <div class="entry"><dt>3D</dt> <dd>is an image of the fetus and its features - So you can see the baby has dad's nose, and mom's lips.</dd></div>
    <div class="entry"><dt>4D</dt> <dd>is 3D, but with motion - You can see baby yawn, move its arm, or even give you a smile.</dd></div>
  </dl>
  <div class="photo" role="img" aria-label="Photo of hands holding an ultrasound print against a pregnant belly"></div>
  <p class="closing"><strong>HD</strong> is also 3D, but better. Now, you can see a rendering of baby's skin, making it the most realistic fetal image possible ... we are one of the few in Los Angeles that have the <strong>newest HD capable machines.</strong></p>
</section>

</body>
</html>
```